Very personalised Wedding Invitation

I want a wedding invitation very unique and personalised with the menus, ceremony time table and thank you cards. I want a mix of a nice traditional style with indian style touch. I don't want a colourful invitation, it can have max. two different colours.

The bride's name is Miranda and the groom's name is Rohan

Reason: None of the designs submitted are what I am looking for

Target Market(s)

Invitations, personalised invitations,

Industry/Entity Type

Wedding

Logo Text

Our initials R&M To use in our wedding things

Font styles to use
Decorative
Script

Requirements
Must have
• -
Nice to have
• I would like a chic design with a bit of indian style
Should not have
• --

```html
<!DOCTYPE html>
<html lang="en">
<head>
<meta charset="utf-8">
<title>Miranda &amp; Rohan — Wedding Invitation</title>
<link rel="stylesheet" href="https://fonts.googleapis.com/css2?family=Cookie&family=Open+Sans:wght@400;700&display=swap">
<style>
  :root {
    --dusk-blue: #99a7bd;
    --blush: #f7cdb8;
    --backdrop: #ffffff;
  }
  html, body {
    margin: 0;
    padding: 0;
    width: 1200px;
    height: 1134px;
    overflow: hidden;
    background: var(--backdrop);
  }
  .canvas {
    position: relative;
    width: 1200px;
    height: 1134px;
  }
  .page {
    position: absolute;
    width: 484px;
    height: 483px;
    background: var(--dusk-blue);
    overflow: hidden;
  }
  .rule {
    position: absolute;
    left: 0;
    right: 0;
    height: 2px;
    background: var(--blush);
  }
  .rule--top { top: 38px; }
  .rule--bottom { top: 443px; }

  .couple {
    position: absolute;
    margin: 0;
    font-family: "Cookie", cursive;
    font-weight: 400;
    color: var(--blush);
    line-height: 1;
  }
  .couple__bride { position: absolute; left: 28px; top: 110px; font-size: 74px; white-space: nowrap; }
  .couple__and { position: absolute; left: 236px; top: 140px; font-size: 70px; }
  .couple__groom { position: absolute; left: 104px; top: 190px; font-size: 78px; white-space: nowrap; }

  .swash {
    position: absolute;
    left: 152px;
    top: 283px;
    width: 62px;
    height: 16px;
  }
  .details {
    position: absolute;
    left: 0;
    width: 332px;
    top: 318px;
    text-align: center;
    font-family: "Open Sans", sans-serif;
    color: var(--blush);
  }
  .details__date { margin: 0; font-weight: 700; font-size: 15px; letter-spacing: 2px; line-height: 18px; }
  .details__place { margin: 10px 0 0; font-weight: 700; font-size: 16px; letter-spacing: 2px; line-height: 18px; }
  .details__note { margin: 6px 0 0; font-weight: 400; font-size: 11px; letter-spacing: 1.5px; line-height: 14px; }

  .mandala-large {
    position: absolute;
    left: 318px;
    top: 66px;
    width: 176px;
    height: 352px;
    border-radius: 176px 0 0 176px;
    background: radial-gradient(circle at 100% 50%, var(--blush) 0%, #d9c3c3 45%, #c6bac6 75%, var(--blush) 100%);
  }
  .mandala-small {
    position: absolute;
    left: 189px;
    top: 188px;
    width: 110px;
    height: 110px;
    border-radius: 50%;
    background: radial-gradient(circle, var(--blush) 0%, #c9bcc6 55%, #d8c4c2 100%);
  }

  .front-card {
    position: absolute;
    left: 368px;
    top: 58px;
    transform-origin: 0 0;
    transform: scale(1.064);
  }
  .spread {
    position: absolute;
    left: 142px;
    top: 617px;
    width: 968px;
    height: 483px;
  }
  .spread .page--back { left: 0; top: 0; }
  .spread .page--cover { left: 484px; top: 0; }
</style>
</head>
<body>
<main class="canvas">

  <section class="page front-card" aria-label="Invitation front">
    <div class="rule rule--top"></div>
    <div class="rule rule--bottom"></div>
    <div class="mandala-large" role="img" aria-label="Half lotus mandala ornament in blush line work"></div>
    <h1 class="couple">
      <span class="couple__bride">Miranda</span>
      <span class="couple__and">&amp;</span>
      <span class="couple__groom">Rohan</span>
    </h1>
    <svg class="swash" viewBox="0 0 62 16" aria-hidden="true">
      <path d="M2 9 C14 2 24 4 32 8 S50 14 60 5" fill="none" stroke="var(--blush)" stroke-width="3" stroke-linecap="round"/>
    </svg>
    <div class="details">
      <p class="details__date">8TH OF JULY 2018</p>
      <p class="details__place">FERNBRIDGE, NY 12410</p>
      <p class="details__note">DINNER AND DANCING TO FOLLOW</p>
    </div>
  </section>

  <section class="spread" aria-label="Invitation open spread">
    <div class="page page--back">
      <div class="rule rule--top"></div>
      <div class="rule rule--bottom"></div>
      <div class="mandala-small" role="img" aria-label="Small lotus mandala ornament in blush line work"></div>
    </div>
    <div class="page page--cover">
      <div class="rule rule--top"></div>
      <div class="rule rule--bottom"></div>
      <div class="mandala-large" role="img" aria-label="Half lotus mandala ornament in blush line work"></div>
      <h2 class="couple">
        <span class="couple__bride">Miranda</span>
        <span class="couple__and">&amp;</span>
        <span class="couple__groom">Rohan</span>
      </h2>
      <svg class="swash" viewBox="0 0 62 16" aria-hidden="true">
        <path d="M2 9 C14 2 24 4 32 8 S50 14 60 5" fill="none" stroke="var(--blush)" stroke-width="3" stroke-linecap="round"/>
      </svg>
      <div class="details">
        <p class="details__date">8TH OF JULY 2018</p>
        <p class="details__place">FERNBRIDGE, NY 12410</p>
        <p class="details__note">DINNER AND DANCING TO FOLLOW</p>
      </div>
    </div>
  </section>

</main>
</body>
</html>
```